Proposal Microsoft Word Template

We are looking for a professional, 5 page document to import our proposals onto. We are looking for a cover page with plenty of color and design built around and utilizing our logo. The remaining four pages should utilize our logo and have some design elements to make it stand apart from other formal proposals. We aren't sure what this looks like yet, so we are open to plenty of ideas. I will upload our logo for your use. We are a fire protection company that sells primarily to other commercial clientele.

First page will be the cover page. This should have our logo prominently placed. A place for the clients name and info.
Second page will be the Executive Summary. Smaller logo, possibly a border on this page, and a clean colorful ribbon on the footer with our information on the bottom. I do like red, blue and black for colors.

Third page will be material lists and pricing information

4th page will consist of detailed scope of work, and exclusions
Fifth page will consist of terms and conditions

Target Market(s)

Commercial Industrial Government Sectors

Requirements
Must have
• Color, clean lines and formatting.

```html
<!DOCTYPE html>
<html lang="en">
<head>
<meta charset="utf-8">
<title>Proposal Template Pages</title>
<link rel="stylesheet" href="https://fonts.googleapis.com/css2?family=Montserrat:wght@700;800&family=Open+Sans:wght@400;600;700&display=swap">
<style>
:root{
  --red:#e0262f;
  --black:#1f1d1e;
  --white:#ffffff;
  --paper:#f7f7f7;
  --stage:#d5d5d5;
  --grey:#b8b8b8;
  --grey-light:#e4e4e6;
  --grey-row:#cfcfd3;
  --text:#333333;
}
*{margin:0;padding:0;box-sizing:border-box}
html,body{width:746px;height:1200px;overflow:hidden}
body{background:var(--stage);font-family:"Open Sans",Arial,sans-serif;color:var(--text);position:relative}
.page{position:absolute;background:var(--paper);box-shadow:0 2px 8px rgba(0,0,0,.25);overflow:hidden}
.cover{left:173px;top:24px;width:400px;height:566px}
.cover-art{position:absolute;left:0;top:0}
.brand{position:absolute;font-family:"Open Sans",Arial,sans-serif;font-weight:700;color:var(--red);letter-spacing:.04em;text-transform:uppercase;white-space:nowrap}
.cover .brand{left:58px;top:78px;font-size:21px}
.brand-mark{display:inline-block;width:.55em;height:.55em;background:var(--red);margin-right:.35em;vertical-align:.08em}
.cover-title{position:absolute;left:40px;right:40px;top:168px;font-family:"Montserrat",Arial,sans-serif;font-weight:800;font-size:21px;line-height:1.25;color:var(--red);text-align:center;text-transform:uppercase}
.ribbon-label{position:absolute;left:20px;top:313px;font-size:9px;color:var(--white)}
.prepared-for{position:absolute;left:262px;top:302px;font-size:8.5px;line-height:1.3;color:var(--white)}
.label-red{color:var(--red);font-weight:700;font-size:9.5px;margin-bottom:2px;line-height:1.3}
.prepared-for strong{font-weight:700}
.prepared-from{position:absolute;left:36px;top:338px;font-size:8px;color:var(--white)}
.details{display:grid;grid-template-columns:92px auto;row-gap:0;line-height:1.2}
.details dt{font-weight:600}
.confidential{position:absolute;left:36px;right:36px;top:452px;font-size:5.6px;line-height:1.35;color:var(--white)}
.confidential .label-red{font-size:9px;margin-bottom:1px}
.cover-web{position:absolute;left:36px;bottom:22px;font-size:11px;font-weight:700;color:var(--black)}
.cover-web span{color:var(--red)}

.inner{top:636px;width:355px;height:502px}
.inner.left{left:18px}
.inner.right{left:373px}
.page-header{position:absolute;left:0;top:0;width:355px;height:48px}
.doc-title{position:absolute;left:14px;top:26px;font-size:8px;color:var(--white)}
.inner .brand{right:14px;top:12px;font-size:8.5px}
.body{position:absolute;left:22px;right:22px;top:58px;font-size:6.3px;line-height:1.45}
.body h2{font-size:10px;color:var(--red);font-weight:700;margin-bottom:6px}
.body p{margin-bottom:7px;text-align:justify}
.page-footer{position:absolute;left:0;bottom:0;width:355px;height:40px}
.footer-info{position:absolute;left:18px;bottom:9px;display:flex;gap:18px;font-size:6.2px;color:var(--white)}
.footer-info span::before{content:"";display:inline-block;width:5px;height:5px;border-radius:50%;background:var(--red);margin-right:4px;vertical-align:0}
.page-no{position:absolute;right:10px;bottom:24px;font-size:7px;font-weight:700;color:var(--white)}

.price-table{width:100%;border-collapse:separate;border-spacing:1px;font-size:5.4px;margin:6px 0 12px;text-align:center}
.price-table th{background:var(--red);color:var(--white);font-weight:600;padding:2px 1px}
.price-table td{background:var(--grey-light);padding:2px 1px}
.price-table tr:nth-child(even) td{background:var(--grey-row)}
.tick-list{list-style:none;margin-top:4px}
.tick-list li{margin-bottom:3px;font-weight:600}
.tick-list li::before{content:"✓";color:var(--red);margin-right:5px;font-weight:700}
.lead{font-weight:700}
</style>
</head>
<body>

<section class="page cover">
  <svg class="cover-art" width="400" height="566" viewBox="0 0 400 566" aria-hidden="true">
    <path d="M0,312 L232,312 C248,312 250,292 266,292 L400,292 L400,482 L266,482 C250,482 248,504 232,504 L0,504 Z" fill="#1f1d1e"/>
    <polygon points="0,312 226,312 216,330 0,330" fill="#e0262f"/>
    <path d="M0,506 L232,506 C248,506 250,486 266,486 L400,486" fill="none" stroke="#e0262f" stroke-width="2"/>
    <rect x="58" y="104" width="290" height="2" fill="#1f1d1e"/>
  </svg>
  <div class="brand"><span class="brand-mark"></span>Bastion Fire and Safety</div>
  <h1 class="cover-title">Title of the proposal<br>document goes here</h1>
  <div class="ribbon-label">Proposal Document</div>

  <div class="prepared-for">
    <div class="label-red">Prepared For:</div>
    <strong>Mark Ellison</strong><br>
    Founder, Northgate Company<br>
    P.O. Box 215, Northgate City<br>
    USA<br>
    E-Mail: mark@northgate.example
  </div>

  <div class="prepared-from">
    <div class="label-red">Prepared From:</div>
    <dl class="details">
      <dt>Offer id:</dt><dd>7608</dd>
      <dt>Dat:</dt><dd>01.10.2018</dd>
      <dt>Valid Until:</dt><dd>31.10.2018</dd>
      <dt>Version:</dt><dd>1</dd>
      <dt>Contact:</dt><dd>Alan Price</dd>
      <dt>Department:</dt><dd>Sales</dd>
      <dt>Phone:</dt><dd>1-800-555-0147</dd>
      <dt>fax:</dt><dd>(800)555-0198</dd>
      <dt>E-Mail:</dt><dd>info@bastionfire.example</dd>
    </dl>
  </div>

  <div class="confidential">
    <div class="label-red">Statement of Confidentiality</div>
    This material in our response and any information disclosed during discussions of this proposal is proprietary and confidential information about our services, methods and processes. Other product names used may be trademarks of their respective owners.
  </div>

  <div class="cover-web">www.<span>bastionfire</span>.example</div>
</section>

<section class="page inner left">
  <svg class="page-header" viewBox="0 0 355 48" aria-hidden="true">
    <rect x="0" y="30" width="355" height="10" fill="#b8b8b8"/>
    <path d="M0,22 L160,22 C170,22 172,40 182,40 L0,40 Z" fill="#1f1d1e"/>
  </svg>
  <div class="doc-title">Document Title</div>
  <div class="brand"><span class="brand-mark"></span>Bastion Fire and Safety</div>
  <div class="body">
    <h2>Executive summary</h2>
    <p>Lorem ipsum dolor sit amet, consectetur adipiscing elit. Aenean semper ut justo sed euismod. Curabitur aliquet nisl ac quam feugiat, eget pharetra erat iaculis. Nullam elementum odio vel lacus imperdiet, ultrices pellentesque augue finibus. Donec ac facilisis tortor, quis commodo nisl.</p>
    <p>Nulla congue lorem sed purus ornare viverra. Ut pretium mi lorem. Ut id odio quis arcu ornare rutrum id a sapien. Mauris tincidunt neque nec leo dignissim fringilla. Curabitur ante sem, vestibulum ac sollicitudin a, euismod vel ipsum. Praesent at diam lacinia, lacinia mi ac, hendrerit nibh.</p>
    <p>Aliquam dictum molestie ipsum, tristique aliquam nulla lobortis nec. Phasellus venenatis rutrum mi. Aliquam vehicula sem ut magna malesuada, dictum bibendum eros tincidunt. Donec aliquet suscipit mi vel consequat. Suspendisse egestas non orci sed luctus.</p>
    <p>Etiam tincidunt nibh nulla, eu fermentum tellus hendrerit in. Sed sollicitudin enim ante, id auctor sem dignissim eget. Curabitur nisi mi, vestibulum non magna quis, suscipit laoreet justo. Phasellus sit amet sollicitudin arcu. Duis eu diam porta, finibus magna eu, finibus eros.</p>
    <p>Curabitur aliquet, elit ut accumsan dignissim, quam enim consequat nisl, dictum congue nulla nisi ac elit. Mauris vel tellus laoreet, mattis ex ut, volutpat lectus. Curabitur pharetra varius urna non facilisis. Etiam sed felis id risus pharetra tempus quis eu nulla.</p>
  </div>
  <svg class="page-footer" viewBox="0 0 355 40" aria-hidden="true">
    <rect x="0" y="20" width="355" height="20" fill="#1f1d1e"/>
    <path d="M300,20 L355,6 L355,20 Z" fill="#e0262f"/>
    <rect x="0" y="18" width="80" height="2" fill="#e0262f"/>
  </svg>
  <div class="footer-info"><span>1-800-555-0147</span><span>info@bastionfire.example</span><span>www.bastionfire.example</span></div>
  <div class="page-no">2</div>
</section>

<section class="page inner right">
  <svg class="page-header" viewBox="0 0 355 48" aria-hidden="true">
    <rect x="0" y="30" width="355" height="10" fill="#b8b8b8"/>
    <path d="M0,22 L160,22 C170,22 172,40 182,40 L0,40 Z" fill="#1f1d1e"/>
  </svg>
  <div class="doc-title">Document Title</div>
  <div class="brand"><span class="brand-mark"></span>Bastion Fire and Safety</div>
  <div class="body">
    <p>Lorem ipsum dolor sit amet, consectetur adipiscing elit. Vestibulum vel ante ac ligula vestibulum hendrerit id eu mi. Vestibulum maximus mattis erat. Quisque lacus mi, volutpat vel justo eu, hendrerit blandit nibh. Nam fermentum nisl sit amet nulla posuere posuere.</p>
    <table class="price-table">
      <thead><tr><th>No.</th><th>Lorem</th><th>Arc. No.</th><th>Phasellus tincidunt</th><th>Quisque</th><th>Ipsum</th></tr></thead>
      <tbody>
        <tr><td>1</td><td>1</td><td>2331</td><td>Consectetur adipiscing elit</td><td>7.450,00 €</td><td>7.450,00 €</td></tr>
        <tr><td>2</td><td>9</td><td>5557</td><td>Praesent eleifend semper velit</td><td>1.460,00 €</td><td>1.290,00 €</td></tr>
        <tr><td>3</td><td>1</td><td>8995</td><td>Quisque vitae tellus nisi</td><td>5.490,00 €</td><td>365,00 €</td></tr>
        <tr><td>4</td><td>2</td><td>7666</td><td>Ut tincidunt nunc turpis</td><td>365,00 €</td><td>390,00 €</td></tr>
        <tr><td>5</td><td>1</td><td>758</td><td>Praesent tincidunt pretium felis</td><td>4.490,00 €</td><td>5.490,00 €</td></tr>
        <tr><td>6</td><td>4</td><td>540</td><td>Pellentesque ut nibh eget</td><td>5.490,00 €</td><td>5.490,00 €</td></tr>
        <tr><td>7</td><td>3</td><td>1945</td><td>Quisque id ipsum lorem</td><td>5.490,00 €</td><td>5.490,00 €</td></tr>
        <tr><td>8</td><td>2</td><td>5890</td><td>Duis rutrum scelerisque</td><td>5.490,00 €</td><td>5.490,00 €</td></tr>
      </tbody>
    </table>
    <p>Lorem ipsum dolor sit amet, consectetur adipiscing elit. Vestibulum vel ante ac ligula vestibulum hendrerit id eu mi. Quisque lacus mi, volutpat vel justo eu, hendrerit.</p>
    <p class="lead">Lorem ipsum dolor sit amet, consectetur adipiscing elit. Vestibulum maximus mattis erat. Nam fermentum nisl sit amet nulla posuere.</p>
    <ul class="tick-list">
      <li>Vestibulum vel ante ac ligula hendrerit id eu mi.</li>
      <li>Donec et pharetra enim. Nam fermentum nisl.</li>
      <li>Fusce consequat lectus dignissim eget.</li>
    </ul>
  </div>
  <svg class="page-footer" viewBox="0 0 355 40" aria-hidden="true">
    <rect x="0" y="20" width="355" height="20" fill="#1f1d1e"/>
    <path d="M300,20 L355,6 L355,20 Z" fill="#e0262f"/>
    <rect x="0" y="18" width="80" height="2" fill="#e0262f"/>
  </svg>
  <div class="footer-info"><span>1-800-555-0147</span><span>info@bastionfire.example</span><span>www.bastionfire.example</span></div>
  <div class="page-no">3</div>
</section>

</body>
</html>
```